Renata Quisby

Luxury And Style -

Black - White & Gold

Target Market(s)

Fashion

Industry/Entity Type

Fashion

Requirements
Must have
• High-End
Nice to have
• We will Print on Silk Paper

```html
<!DOCTYPE html>
<html lang="en">
<head>
<meta charset="utf-8">
<title>Renata Quisby — Letterhead</title>
<link rel="stylesheet" href="https://fonts.googleapis.com/css2?family=Cinzel:wght@400&family=Montserrat:wght@400;500&display=swap">
<style>
  :root {
    --ink: #0b0b0b;
    --gold: #d9a63a;
    --gold-soft: #e3b44e;
    --gold-pale: #f6e6c2;
    --paper: #ffffff;
  }
  * { margin: 0; padding: 0; box-sizing: border-box; }
  html, body { width: 848px; height: 1200px; overflow: hidden; background: var(--paper); }
  .letterhead { position: relative; width: 848px; height: 1200px; background: var(--paper); }
  .letterhead__art,
  .accent-area { position: absolute; inset: 0; width: 848px; height: 1200px; display: block; }
  .brand {
    position: absolute; left: 62px; top: 58px; width: 270px;
    text-align: center; color: var(--gold);
  }
  .brand__dot {
    display: block; width: 44px; height: 44px; margin: 0 auto 14px;
    border: 2px solid var(--gold); border-radius: 50%;
  }
  .brand__name {
    font-family: "Cinzel", serif; font-weight: 400;
    font-size: 23px; letter-spacing: 2px; line-height: 1;
  }
  .brand__tagline {
    margin-top: 8px;
    font-family: "Montserrat", sans-serif; font-weight: 400;
    font-size: 10px; letter-spacing: 1.2px; line-height: 1;
  }
  .contact {
    position: absolute; top: 1130px;
    font-family: "Montserrat", sans-serif; font-weight: 500;
    font-size: 14px; letter-spacing: 1.4px; line-height: 26px;
    color: var(--gold-soft);
  }
  .contact--address { left: 405px; }
  .contact--web { left: 598px; }
  .contact__divider {
    position: absolute; left: 573px; top: 1126px;
    width: 1.5px; height: 60px; background: var(--paper);
  }
</style>
</head>
<body>
<main class="letterhead">
  <svg class="accent-area accent-area--top" viewBox="0 0 387 545" preserveAspectRatio="none"
       role="img" aria-label="Decorative gold line pattern beneath the header wave">
    <defs>
      <linearGradient id="top-accent-fill" x1="0" y1="0" x2="1" y2="1">
        <stop offset="0" stop-color="var(--gold-pale)" stop-opacity="0.9"/>
        <stop offset="1" stop-color="var(--gold-pale)" stop-opacity="0"/>
      </linearGradient>
    </defs>
    <path fill="url(#top-accent-fill)"
          d="M0,66 C10,72 24,80 38,86 C66,100 98,104 122,90 L0,175 Z"/>
  </svg>

  <svg class="accent-area accent-area--bottom" viewBox="0 0 387 545" preserveAspectRatio="none"
       role="img" aria-label="Decorative gold line pattern above the footer wave">
    <defs>
      <linearGradient id="bottom-accent-fill" x1="1" y1="0" x2="0" y2="1">
        <stop offset="0" stop-color="var(--gold-pale)" stop-opacity="0.9"/>
        <stop offset="1" stop-color="var(--gold-pale)" stop-opacity="0"/>
      </linearGradient>
    </defs>
    <path fill="url(#bottom-accent-fill)"
          d="M387,426 L270,468 C300,456 340,458 387,478 Z"/>
  </svg>

  <svg class="letterhead__art" viewBox="0 0 387 545" preserveAspectRatio="none" aria-hidden="true">
    <path class="header-black" fill="var(--ink)"
          d="M0,0 H244 L122,88 C100,100 70,96 40,78 C25,70 10,62 0,57 Z"/>
    <path class="header-band" fill="var(--gold)"
          d="M0,57 C10,62 25,70 40,78 C70,96 100,100 122,88 L126,86 L124,89 C98,104 66,100 38,86 C24,80 10,72 0,66 Z"/>

    <path class="frame-right" fill="none" stroke="var(--gold)" stroke-width="0.7"
          d="M252,10 H367 Q374,10 374,17 V420"/>
    <path class="frame-left" fill="none" stroke="var(--gold)" stroke-width="0.7"
          d="M10,183 V528 Q10,535 17,535 H54"/>

    <path class="footer-black" fill="var(--ink)"
          d="M78,545 L278,476 C305,466 345,468 387,486 V545 Z"/>
    <path class="footer-band" fill="var(--gold)"
          d="M58,545 L270,468 C300,456 340,458 387,478 V486 C345,468 305,466 278,476 L78,545 Z"/>
  </svg>

  <header class="brand">
    <span class="brand__dot"></span>
    <h1 class="brand__name">RENATA QUISBY</h1>
    <p class="brand__tagline">LUXURY AND STYLE</p>
  </header>

  <footer>
    <p class="contact contact--address">ATELIER ROW, 48<br>+12 555 014 220</p>
    <span class="contact__divider"></span>
    <p class="contact contact--web">WWW.QUISBYSTYLE.COM<br>HELLO@QUISBYSTYLE.COM</p>
  </footer>
</main>
</body>
</html>
```